Lanterne architecture business cards

We are a new company based in New Zealand. We Specialize in High end Luxury Residential Architecture.

Every home is bespoke and is designed to each clients individual requirements and needs.

I like to design buildings that inspire people through light and form while offering a high level of comfort and usability.

Lines of sight, proportion and balance are fundamental to the spaces I create.
Updates

August 5th is current deadline - Today's date is the 13th of August.

Target Market(s)

New Zealanders who want a custom individual home design, typically 30-65 year old males and females

Industry/Entity Type

Architecture

Contact Information for Business Card

Director - Derek Tolson
Contact Number - 0279164073
Email - info@lanternearchitecture-example.co.nz
Webstie - www.lanternearchitecture-example.co.nz
Social Media - @lanternearchitecture

Font styles to use
Sans Serif

Requirements
Must have
• Logo (Both Sides)
Website
Email
Contact Number
Social Media

Nice to have
• Texture
Should not have
• More than 3 colours - typically I would've thought 2 would be good to match the logo.

```html
<!DOCTYPE html>
<html lang="en">
<head>
<meta charset="utf-8">
<title>Lanterne architecture business cards</title>
<link rel="stylesheet" href="https://fonts.googleapis.com/css2?family=Josefin+Sans:wght@300;400&family=Open+Sans:wght@400&display=swap">
<style>
  :root {
    --backdrop: #f0f0f0;
    --card: #ffffff;
    --ink: #111111;
    --mark: #262626;
    --shadow: rgba(0, 0, 0, 0.28);
  }
  * { box-sizing: border-box; margin: 0; padding: 0; }
  html, body {
    width: 1200px; height: 1200px; overflow: hidden;
    background: var(--backdrop);
  }
  .sheet { position: relative; width: 1200px; height: 1200px; }

  .card {
    position: absolute;
    width: 675px; height: 405px;
    background: var(--card);
    box-shadow: 2px 4px 5px var(--shadow);
    overflow: hidden;
  }
  .card--front { left: 192px; top: 134px; }
  .card--back  { left: 188px; top: 611px; }

  /* brand lockup: plain disc + spaced name */
  .brand-disc { position: absolute; border-radius: 50%; background: var(--mark); }
  .wordmark {
    position: absolute;
    font-family: "Josefin Sans", sans-serif;
    font-weight: 300;
    color: var(--ink);
    display: flex; justify-content: space-between;
    line-height: 1;
  }
  .wordmark--name { font-size: 24px; }
  .wordmark--sub  { font-size: 7px; }

  .card--front .brand-disc { left: 263px; top: 87px; width: 150px; height: 150px; }
  .card--front .wordmark   { left: 208px; width: 260px; }
  .card--front .wordmark--name { top: 263px; }
  .card--front .wordmark--sub  { top: 292px; }

  .card--back .brand-disc { left: 98px; top: 77px; width: 150px; height: 150px; }
  .card--back .wordmark   { left: 53px; width: 259px; }
  .card--back .wordmark--name { top: 254px; }
  .card--back .wordmark--sub  { top: 283px; }

  .divider {
    position: absolute; left: 333px; top: 82px;
    width: 4px; height: 226px; background: var(--ink);
  }
  .person-name {
    position: absolute; left: 398px; top: 106px;
    font-family: "Josefin Sans", sans-serif; font-weight: 300;
    font-size: 30px; color: var(--ink); white-space: nowrap;
  }
  .person-role {
    position: absolute; left: 406px; top: 139px;
    font-family: "Josefin Sans", sans-serif; font-weight: 400;
    font-size: 13px; letter-spacing: 0.5px; color: var(--ink);
  }
  .role-rule {
    position: absolute; left: 407px; top: 163px;
    width: 46px; height: 5px; background: var(--ink);
  }
  .contact-list { list-style: none; }
  .contact-item {
    position: absolute; left: 373px;
    display: flex; align-items: center; gap: 10px;
    font-family: "Open Sans", sans-serif; font-size: 12px;
    color: var(--ink); white-space: nowrap;
  }
  .contact-item svg { width: 22px; height: 20px; flex: none; }
  .contact-item--phone { top: 189px; }
  .contact-item--mail  { top: 214px; }
  .contact-item--web   { top: 239px; }
  .social-marker {
    position: absolute; left: 505px; top: 318px;
    width: 14px; height: 14px; background: var(--ink);
  }
  .social-handle {
    position: absolute; left: 412px; width: 200px; top: 337px;
    text-align: center;
    font-family: "Open Sans", sans-serif; font-size: 13px; color: var(--ink);
  }

  .loose-lockup { position: absolute; left: 953px; top: 1010px; width: 200px; height: 170px; }
  .loose-lockup .brand-disc { left: 42px; top: 0; width: 116px; height: 116px; background: var(--ink); }
  .loose-lockup .wordmark { left: 0; width: 200px; }
  .loose-lockup .wordmark--name { top: 136px; font-size: 19px; }
  .loose-lockup .wordmark--sub  { top: 159px; font-size: 6px; }
</style>
</head>
<body>
<main class="sheet">

  <section class="card card--front" aria-label="Card front">
    <div class="brand-disc"></div>
    <div class="wordmark wordmark--name"><span>L</span><span>A</span><span>N</span><span>T</span><span>E</span><span>R</span><span>N</span><span>E</span></div>
    <div class="wordmark wordmark--sub"><span>A</span><span>R</span><span>C</span><span>H</span><span>I</span><span>T</span><span>E</span><span>C</span><span>T</span><span>U</span><span>R</span><span>E</span></div>
  </section>

  <section class="card card--back" aria-label="Card back">
    <div class="brand-disc"></div>
    <div class="wordmark wordmark--name"><span>L</span><span>A</span><span>N</span><span>T</span><span>E</span><span>R</span><span>N</span><span>E</span></div>
    <div class="wordmark wordmark--sub"><span>A</span><span>R</span><span>C</span><span>H</span><span>I</span><span>T</span><span>E</span><span>C</span><span>T</span><span>U</span><span>R</span><span>E</span></div>

    <div class="divider"></div>

    <h1 class="person-name">Derek Tolson</h1>
    <p class="person-role">Director</p>
    <div class="role-rule"></div>

    <ul class="contact-list">
      <li class="contact-item contact-item--phone">
        <svg viewBox="0 0 22 20" aria-hidden="true"><path d="M2 12 Q2 5 11 5 Q20 5 20 12 L16 13 L15 10 Q11 8.5 7 10 L6 13 Z" fill="#222"/></svg>
        <span>0279164073</span>
      </li>
      <li class="contact-item contact-item--mail">
        <svg viewBox="0 0 22 20" aria-hidden="true"><rect x="1.5" y="4" width="19" height="13" fill="none" stroke="#222" stroke-width="1.6"/><path d="M1.5 4 L11 11.5 L20.5 4 M1.5 17 L8.5 10 M20.5 17 L13.5 10" fill="none" stroke="#222" stroke-width="1.4"/></svg>
        <span>info@lanternearchitecture-example.co.nz</span>
      </li>
      <li class="contact-item contact-item--web">
        <svg viewBox="0 0 22 20" aria-hidden="true"><g fill="none" stroke="#333" stroke-width="1"><circle cx="11" cy="10" r="8.5"/><ellipse cx="11" cy="10" rx="4" ry="8.5"/><path d="M11 1.5 V18.5 M2.5 10 H19.5 M4 5.5 H18 M4 14.5 H18"/></g></svg>
        <span>www.lanternearchitecture-example.co.nz</span>
      </li>
    </ul>

    <div class="social-marker" aria-hidden="true"></div>
    <p class="social-handle">@lanternearchitecture</p>
  </section>

  <div class="loose-lockup" aria-label="Lanterne architecture">
    <div class="brand-disc"></div>
    <div class="wordmark wordmark--name"><span>L</span><span>A</span><span>N</span><span>T</span><span>E</span><span>R</span><span>N</span><span>E</span></div>
    <div class="wordmark wordmark--sub"><span>A</span><span>R</span><span>C</span><span>H</span><span>I</span><span>T</span><span>E</span><span>C</span><span>T</span><span>U</span><span>R</span><span>E</span></div>
  </div>

</main>
</body>
</html>
```